Graphic Design of Business Process

We require an eye-catching, sophisticated design of 2 business processes (attached), that will be used digitally AND for print (to be put on walls in our office).

The basic layout is attached. We require a creative, professional designer to re-design these so that they look appealing but still able to grasp all the information.

We will require vector files and editable project files for final delivery. You may refer to our website (lanternwickhub.com.au) for an indication of our brand.

If you have any questions, please ask.

Thank you.

```html
<!DOCTYPE html>
<html lang="en">
<head>
<meta charset="UTF-8">
<title>Content Heirarchy</title>
<link href="https://fonts.googleapis.com/css2?family=Montserrat:wght@300;400;700&display=swap" rel="stylesheet">
<style>
  :root {
    --ink: #000000;
    --paper: #ffffff;
    --gold: #c2a906;
    --tier-hero: #d0ba3b;
    --tier-hub: #c2a906;
    --tier-hygiene: #937e05;
  }
  * { margin: 0; padding: 0; box-sizing: border-box; }
  html, body {
    width: 1200px;
    height: 1198px;
    overflow: hidden;
    background: var(--paper);
  }
  .poster {
    position: relative;
    width: 1200px;
    height: 1198px;
    font-family: "Montserrat", Arial, sans-serif;
  }
  .poster-title {
    position: absolute;
    top: 58px;
    left: 0;
    width: 1200px;
    text-align: center;
    font-weight: 700;
    font-size: 91px;
    line-height: 1;
    letter-spacing: 0.5px;
    color: var(--ink);
  }
  .poster-title .accent { color: var(--gold); }
  .stack { position: absolute; left: 0; top: 0; }
  .spine { fill: var(--ink); }
  .tier-hero { fill: var(--tier-hero); }
  .tier-hub { fill: var(--tier-hub); }
  .tier-hygiene { fill: var(--tier-hygiene); }
  .tier-name {
    font-family: "Montserrat", Arial, sans-serif;
    font-weight: 700;
    font-size: 70px;
    fill: var(--paper);
    text-anchor: middle;
  }
  .tier-note {
    font-family: "Montserrat", Arial, sans-serif;
    font-weight: 300;
    font-size: 29px;
    fill: var(--paper);
  }
  .tier-note .strong { font-weight: 700; }
  .divider { stroke: var(--paper); stroke-width: 2; }
</style>
</head>
<body>
<main class="poster">
  <h1 class="poster-title">CONTENT <span class="accent">HEIRARCHY</span></h1>

  <svg class="stack" width="1200" height="1198" viewBox="0 0 1200 1198" aria-label="Content tiers: Hero, Hub, Hygiene">
    <rect class="spine" x="334" y="309" width="500" height="41"/>
    <rect class="spine" x="334" y="582" width="500" height="35"/>
    <rect class="spine" x="334" y="849" width="500" height="34"/>

    <g class="tier">
      <rect class="tier-hero" x="270" y="349" width="628" height="233"/>
      <text class="tier-name" x="584" y="452">HERO</text>
      <line class="divider" x1="387" y1="480" x2="387" y2="538"/>
      <text class="tier-note" x="413" y="522">TENTPOLE <tspan class="strong">CAMPAIGNS</tspan></text>
    </g>

    <g class="tier">
      <rect class="tier-hub" x="270" y="616" width="628" height="233"/>
      <text class="tier-name" x="584" y="724">HUB</text>
      <line class="divider" x1="346" y1="743" x2="346" y2="801"/>
      <text class="tier-note" x="372" y="786">REGULAR <tspan class="strong">“PUSH” CONTENT</tspan></text>
    </g>

    <g class="tier">
      <rect class="tier-hygiene" x="270" y="882" width="628" height="233"/>
      <text class="tier-name" x="584" y="990">HYGIENE</text>
      <line class="divider" x1="334" y1="1018" x2="334" y2="1075"/>
      <text class="tier-note" x="357" y="1061">ALWAYS  ON <tspan class="strong">“PULL” CONTENT</tspan></text>
    </g>
  </svg>
</main>
</body>
</html>
```